Home brewer beer bottle label

I need a label for home-brew beer bottles. My sons and I all make our own beer. It should say Kessner Ale in blackletter (because we are of German heritage) (EDIT: ACTUALLY WE ARE LIKING OTHER TYPEFACE NOW) and the designer will need to work in aspects of the Kessner family (crest attached). Finally we will need two blank areas or lines for (1) what kind of beer (handwritten) and (2) who made it (the Beerista!) I have attached a rough sketch, but feel free to ignore and be creative. No color requirements. (EDIT: ACTUALLY, MY WIFE LIKES THE LITTLE BIT OF PURPLE IN THE 4TH DESIGN) Would like the logotype portion of the label to be usable on its own as a family logo. (EDIT; THIS IS LESS IMPORTANT NOW). I have attached another file sketch, which shows using the parts of the family crest w/out trying to replicate it. Thanks, everyone, for the good work....
Updates

Project Deadline Extended
Reason: Extending because my wife is out of town until Wednesday and I need her input.

Target Market(s)

Mostly friends and family at the wedding.

Industry/Entity Type

Work

Font styles to use
Serif
Sans Serif

Requirements
Must have
• Tightly kerned lettering,
Nice to have
• Color, one Group of Elements in Indesign and the print file, "Beer" and "Beerista" lines
Should not have
• Hard to see logo or logo type

```html
<!DOCTYPE html>
<html lang="en">
<head>
<meta charset="utf-8">
<title>Kessner Ale – Bottle Label</title>
<link href="https://fonts.googleapis.com/css2?family=Alfa+Slab+One&family=Fira+Sans+Condensed:wght@700&display=swap" rel="stylesheet">
<style>
  :root {
    --khaki: #cec47f;
    --khaki-light: #d8cf8c;
    --ink: #1b1a17;
    --band-blue: #3947a0;
    --art-blue: #4a66b0;
    --art-gold: #d9bd5a;
  }
  html, body {
    margin: 0;
    padding: 0;
    width: 988px;
    height: 1200px;
    overflow: hidden;
    background: #ffffff;
  }
  .label {
    position: relative;
    width: 988px;
    height: 1200px;
  }
  .label-shape {
    position: absolute;
    inset: 0;
  }
  .crest-art {
    position: absolute;
    left: 250px;
    top: 104px;
    width: 490px;
    height: 480px;
    border-radius: 24px;
    background: linear-gradient(160deg, var(--art-gold) 0%, var(--art-blue) 100%);
    opacity: 0.85;
  }
  .brand-name {
    position: absolute;
    left: 0;
    right: 0;
    top: 620px;
    margin: 0;
    text-align: center;
    font-family: "Alfa Slab One", serif;
    font-weight: 400;
    font-size: 150px;
    line-height: 156px;
    letter-spacing: -0.02em;
    color: var(--ink);
  }
  .brand-name span { display: block; }
  .family-band {
    position: absolute;
    left: 40px;
    top: 1002px;
    width: 908px;
    height: 70px;
    background: var(--band-blue);
    display: flex;
    align-items: center;
    justify-content: center;
    font-family: "Fira Sans Condensed", sans-serif;
    font-weight: 700;
    font-size: 37px;
    color: var(--khaki-light);
  }
  .field-label {
    position: absolute;
    top: 1102px;
    font-family: "Fira Sans Condensed", sans-serif;
    font-weight: 700;
    font-size: 32px;
    line-height: 40px;
    color: var(--ink);
  }
  .field-beer { left: 60px; }
  .field-beerista { left: 526px; }
</style>
</head>
<body>
<div class="label">
  <svg class="label-shape" width="988" height="1200" viewBox="0 0 988 1200" aria-hidden="true">
    <path d="M0 396 H58 A436 396 0 0 1 930 396 H988 V1200 H0 Z" fill="var(--khaki)"/>
    <path d="M24 1176 V422 H146 A348 396 0 0 1 842 422 H964 V1176 Z" fill="none" stroke="var(--ink)" stroke-width="8"/>
  </svg>

  <div class="crest-art" role="img" aria-label="Family crest artwork"></div>

  <h1 class="brand-name"><span>Kessner</span><span>Ale</span></h1>

  <div class="family-band">Home-Brewed by the Kessner Family</div>

  <div class="field-label field-beer">Beer</div>
  <div class="field-label field-beerista">Beerista</div>
</div>
</body>
</html>
```